Urine collection cup with and without sterile seal sticker

Hello. We need a urine cup label designed please with

Name:
Date of Birth:
Date:
Time:
Temp℃:
Specimen ID:

Product code: TUB-47
Volume markings (e.g., 30 mL, 60 mL, 90 mL).
Vela Drug Tests logo

Could you please provide one version with the additional sterile sticker extending to the top, and one version without the additional sterile sticker?

```html
<!DOCTYPE html>
<html lang="en">
<head>
<meta charset="utf-8">
<title>Urine Collection Cup Label – Vela Drug Tests</title>
<link rel="stylesheet" href="https://fonts.googleapis.com/css2?family=Bebas+Neue&display=swap">
<style>
  :root {
    --label-yellow: #F2D612;
    --brand-blue: #56A0D3;
    --ink-black: #000000;
    --paper-white: #FFFFFF;
  }
  * { margin: 0; padding: 0; box-sizing: border-box; }
  html, body {
    width: 879px; height: 1200px; overflow: hidden;
    background: var(--paper-white);
  }
  .label {
    position: relative; width: 879px; height: 1200px;
    font-family: "Bebas Neue", "Oswald", sans-serif;
    color: var(--brand-blue);
    line-height: 1;
  }
  .label-body {
    position: absolute; left: 54px; top: 225px;
    width: 769px; height: 917px;
    background: var(--label-yellow);
  }
  .sterile-tab {
    position: absolute; left: 695px; top: 55px;
    width: 128px; height: 200px;
    background: var(--label-yellow);
    border-radius: 56px 56px 0 0;
  }
  .sterile-text {
    position: absolute; left: 760px; top: 179px;
    transform: translate(-50%, -50%) rotate(-90deg);
    font-size: 67px; letter-spacing: 2px;
    white-space: nowrap;
  }
  .title-bar {
    position: absolute; left: 136px; top: 355px;
    width: 607px; height: 125px;
    background: var(--ink-black);
    display: flex; align-items: center; justify-content: center;
  }
  .title-bar h1 {
    font-weight: 400; font-size: 74px; letter-spacing: 1px;
    padding-top: 6px;
  }
  .fields {
    position: absolute; left: 136px; top: 515px;
    width: 607px; list-style: none;
  }
  .field {
    display: flex; height: 59px; margin-bottom: 20.2px;
    border: 8px solid var(--ink-black);
  }
  .field-name {
    width: 254px; background: var(--label-yellow);
    font-size: 46px; padding: 2px 0 0 22px;
    display: flex; align-items: center;
  }
  .field-entry { flex: 1; background: var(--paper-white); }
  .product-bar {
    position: absolute; left: 135px; top: 1008px;
    width: 607px; height: 125px;
    background: var(--ink-black);
  }
  .product-code {
    position: absolute; left: 21px; top: 14px; font-size: 46px;
  }
  .rule {
    position: absolute; top: 60px; height: 3px;
    background: var(--brand-blue);
  }
  .rule-left { left: 20px; width: 190px; }
  .rule-right { left: 383px; width: 204px; }
  .brand {
    position: absolute; left: 222px; top: 48px;
    display: flex; align-items: center; gap: 7px;
  }
  .brand-dot {
    width: 26px; height: 26px; border-radius: 50%;
    background: var(--brand-blue);
  }
  .brand-name { font-size: 21px; padding-top: 2px; white-space: nowrap; }
  .volume {
    position: absolute; right: 20px; top: 76px; font-size: 46px;
  }
</style>
</head>
<body>
<div class="label">
  <div class="sterile-tab"></div>
  <div class="label-body"></div>
  <div class="sterile-text">STERILE</div>

  <header class="title-bar"><h1>URINE COLLECTION CUP</h1></header>

  <ul class="fields">
    <li class="field"><span class="field-name">NAME</span><span class="field-entry"></span></li>
    <li class="field"><span class="field-name">DATE OF BIRTH</span><span class="field-entry"></span></li>
    <li class="field"><span class="field-name">DATE</span><span class="field-entry"></span></li>
    <li class="field"><span class="field-name">TIME</span><span class="field-entry"></span></li>
    <li class="field"><span class="field-name">TEMP °C</span><span class="field-entry"></span></li>
    <li class="field"><span class="field-name">SPECIMEN ID</span><span class="field-entry"></span></li>
  </ul>

  <footer class="product-bar">
    <span class="product-code">TUB-47</span>
    <span class="rule rule-left"></span>
    <div class="brand">
      <span class="brand-dot"></span>
      <span class="brand-name">VELA DRUG TESTS</span>
    </div>
    <span class="rule rule-right"></span>
    <span class="volume">90 ML</span>
  </footer>
</div>
</body>
</html>
```